Flyer Design Project

I need a cool design that describes a new line of services I am selling. The final product should be a 8 1/2 by 11 and maximum two pages.

I am selling consulting services to learn to use web conferencing tools for business development, meeting and training.
Updates

Please use the file I have attached as a guide for your work. It is a document called "ebook-costsavingtips" and I love its design.

Thanks

                                        Please substitute the new text availble and just uploaded in the FLYER. Please submit the FINAL version fo your design with TExt changes as well as improvements detailed in previous message. 

Target Market(s)

Entrepreneurs and classroom educators who wnats to explore a new way to teach (innovators not scared of technology)

Industry/Entity Type

Business

Requirements
Must have
• I would like to receive a final PDF with the content EDITABLE for minor edits (I have acrobat)
Logo should be included (attached)

PLEASE CHECK OUT ATTACHED DOCUMENT WHOSE DESIGN I LOVE.
IT is called "Ebook cost-savings tips". If you could follow that as a template to design mine that would be great!

```html
<!DOCTYPE html>
<html lang="en">
<head>
<meta charset="utf-8">
<title>Online Meeting Skills Services – Flyer</title>
<link href="https://fonts.googleapis.com/css2?family=Arimo:wght@400;700&display=swap" rel="stylesheet">
<style>
  :root {
    --orange: #f07d1a;
    --orange-deep: #e8691b;
    --yellow: #f6c315;
    --amber: #f3a21c;
    --red: #dc3a1e;
    --crimson: #b5221a;
    --maroon: #8e1512;
    --ink: #1f1f1f;
    --grey-line: #c9c9c9;
    --tint-1: #fff8e2;
    --tint-2: #fef1e0;
    --tint-3: #fde9db;
    --tint-4: #fde1d4;
    --paper: #ffffff;
  }
  * { box-sizing: border-box; margin: 0; padding: 0; }
  html, body { width: 1200px; height: 829px; overflow: hidden; background: var(--paper); }
  body { font-family: "Arimo", Arial, sans-serif; color: var(--ink); position: relative; }

  .page { position: absolute; top: 0; height: 829px; width: 586px; background: var(--paper); border: 1px solid var(--grey-line); overflow: hidden; }
  .page--front { left: 0; }
  .page--back { left: 614px; }

  .page-curve { position: absolute; inset: 0; width: 100%; height: 100%; pointer-events: none; }

  .brand { position: absolute; top: 38px; right: 32px; text-align: right; }
  .brand__name { display: flex; align-items: center; justify-content: flex-end; gap: 6px; font-size: 21px; font-weight: 700; color: #2b2b2b; letter-spacing: 0.3px; line-height: 1; }
  .brand__dot { width: 10px; height: 10px; border-radius: 50%; background: var(--orange); }
  .brand__tagline { font-size: 9px; color: #2b2b2b; margin-top: 7px; letter-spacing: 0.2px; }

  /* Front page */
  .hero { position: absolute; top: 100px; left: 0; width: 586px; height: 242px; }
  .hero__visual { position: absolute; inset: 0; background:
      radial-gradient(ellipse 200px 70px at 390px 95px, rgba(255,226,150,0.85), rgba(214,124,32,0.35) 55%, transparent 80%),
      linear-gradient(100deg, #1a0f06 0%, #3b2008 40%, #6a3d10 70%, #2d1a07 100%); }
  .hero__tab { position: absolute; top: 0; left: 0; width: 586px; height: 242px; }
  .hero__title { position: absolute; left: 105px; top: 82px; color: #fff; font-weight: 700; line-height: 0.93; }
  .hero__line { display: block; font-size: 42px; letter-spacing: 0.6px; }
  .hero__line--small { font-size: 27px; margin-top: 4px; letter-spacing: 0.4px; }
  .hero__sub { display: block; font-size: 17px; margin-top: 7px; }

  .callout { position: absolute; left: 160px; top: 350px; width: 426px; height: 56px; background: var(--orange); border-radius: 14px 0 0 14px; color: #fff; font-weight: 700; font-size: 16px; line-height: 20px; padding: 8px 16px; }

  .intro { position: absolute; left: 160px; top: 418px; width: 402px; font-size: 10.1px; line-height: 13.5px; text-align: justify; }
  .intro p { margin-bottom: 6px; }

  .points { position: absolute; left: 160px; top: 583px; width: 426px; list-style: none; }
  .point { border-left: 10px solid; border-bottom: 1px solid #f0c9a8; font-size: 10.1px; line-height: 13.4px; padding: 6px 14px 6px 8px; }
  .point::before, .service::before { content: "➥"; color: var(--orange-deep); margin-right: 6px; }
  .point--1 { border-left-color: var(--yellow); background: var(--tint-1); height: 52px; }
  .point--2 { border-left-color: var(--amber); background: var(--tint-2); height: 38px; }
  .point--3 { border-left-color: var(--orange-deep); background: var(--tint-3); height: 38px; }
  .point--4 { border-left-color: var(--red); background: var(--tint-4); height: 52px; }

  /* Back page */
  .headline { position: absolute; left: 161px; top: 97px; width: 355px; color: var(--orange); font-weight: 700; font-size: 15.4px; line-height: 22px; }
  .services { position: absolute; left: 160px; top: 166px; width: 416px; list-style: none; }
  .service { border-left: 10px solid; border-bottom: 1px solid #f0c9a8; font-size: 9.7px; line-height: 13.4px; padding: 6px 10px 5px 8px; text-align: justify; }
  .service--1 { border-left-color: var(--yellow); background: var(--tint-1); height: 94px; }
  .service--2 { border-left-color: var(--amber); background: var(--tint-2); height: 80px; }
  .service--3 { border-left-color: var(--orange); background: var(--tint-2); height: 66px; }
  .service--4 { border-left-color: var(--orange-deep); background: var(--tint-3); height: 66px; }
  .service--5 { border-left-color: var(--red); background: var(--tint-4); height: 69px; }
  .service--6 { border-left-color: var(--crimson); background: var(--tint-4); height: 54px; }
  .service--7 { border-left-color: var(--maroon); background: var(--tint-4); height: 48px; }

  .closing { position: absolute; left: 161px; top: 648px; width: 412px; font-size: 9.9px; line-height: 13.4px; text-align: justify; }
  .closing p { margin-bottom: 1px; }

  .contact-bar { position: absolute; left: 0; bottom: 0; width: 586px; height: 56px; background: var(--orange); color: #fff; text-align: right; padding: 16px 14px 0 0; font-size: 13px; }
  .contact-bar strong { font-weight: 700; }
  .contact-bar__phone { font-size: 19px; font-weight: 700; }
</style>
</head>
<body>

<section class="page page--front">
  <svg class="page-curve" viewBox="0 0 586 829" aria-hidden="true">
    <path d="M140 0 C 20 230, 20 560, 185 829" fill="none" stroke="var(--orange)" stroke-width="1.3"/>
  </svg>

  <div class="brand">
    <div class="brand__name"><span class="brand__dot"></span>Partake Consulting</div>
    <div class="brand__tagline">Learning. Teamwork. Growth.</div>
  </div>

  <div class="hero">
    <div class="hero__visual" role="img" aria-label="Dark screen of glowing program code with a bright light swirl"></div>
    <svg class="hero__tab" viewBox="0 0 586 242" aria-hidden="true">
      <path d="M0 0 H 95 C 70 80, 60 160, 60 242 H 0 Z" fill="var(--orange)"/>
    </svg>
    <h1 class="hero__title">
      <span class="hero__line">ONLINE</span>
      <span class="hero__line">MEETING</span>
      <span class="hero__line hero__line--small">SKILLS SERVICES</span>
      <span class="hero__sub">It is just the beginning...</span>
    </h1>
  </div>

  <div class="callout">What if your business can reach all the people already interested in learning what you know?</div>

  <div class="intro">
    <p>A different use of webinar technology: the first step towards a new way of thinking about your markets/your clients.</p>
    <p>You probably know about webinars. You may have attended a few yourself. Perhaps you found them boring and un-engaging, with no chance to interact or ask questions to a guarded speaker. Did the speaker drone on as you – yes, you! – checked your email? Good news: we are not talking about "that" kind of webinars. Yes: there is another way!</p>
    <p>Turn your expertise into engaging and interactive online sessions delivered "live"! Engage people online in conversations that matter to them and forget about the technical details, the mailing list or selecting the right webinar technology. We can provide a turnkey solution, that in two-week time offers you all you need to break into this new technology from the front-door. In fact:</p>
  </div>

  <ul class="points">
    <li class="point point--1">We design an effective virtual meeting experience for you using the tools of the online room to their full potential through a different way of thinking about online participant engagement and interactivity.</li>
    <li class="point point--2">We repurpose your marketing materials for engaging collaborative online meeting and learning.</li>
    <li class="point point--3">We develop and execute a communication plan to market your online sessions to your mailing list - already interested in learning about your expertise – and to others.</li>
    <li class="point point--4">We support you "hands-on" as you deliver a synchronous (live and online) session in your own virtual training room. We orchestrate a rehearsal and you show up on the day of the session ready to engage your remote participants.</li>
  </ul>
</section>

<section class="page page--back">
  <svg class="page-curve" viewBox="0 0 586 829" aria-hidden="true">
    <path d="M165 0 C 30 220, 20 560, 150 829" fill="none" stroke="var(--orange)" stroke-width="1.3"/>
  </svg>

  <div class="brand">
    <div class="brand__name"><span class="brand__dot"></span>Partake Consulting</div>
    <div class="brand__tagline">Learning. Teamwork. Growth.</div>
  </div>

  <h2 class="headline">Choose the service that best fit your needs and budget. A new level of online engagement and virtual collaboration awaits.</h2>

  <ul class="services">
    <li class="service service--1">Webinar Series: Plan, design, develop and implement a 3+1 session webinar series about the content of your expertise marketed to live audiences with 3 hours of One-on-One online coaching on web conferencing tools and how to use them for your business. Includes access to online resource library of our Online Facilitator Certification plus access to your own online meeting room and virtual collaboration platform ($3,000).</li>
    <li class="service service--2">Webinar: Plan, design, develop and implement 1 webinar session on the content of your expertise marketed to live audiences with 3 hours of One-on-One online coaching on web conferencing tools and how to use them for your business. Includes access to online resource library of our Online Facilitator Certification plus access to your own online meeting room and virtual collaboration platform ($1,900).</li>
    <li class="service service--3">Outfitting the Online Entrepreneur: 4-hours of One-on-One online coaching to learn about web conferencing tools and how to use them for your business. Includes access to online resource library of our Online Facilitator Certification plus access to your own online meeting room and virtual collaboration platform ($1,300).</li>
    <li class="service service--4">Outfitting the Online Educator: 3-hours of One-on-One online coaching to learn about web conferencing tools and how to use them for your training sessions. Includes access to online resource library of our Online Facilitator Certification plus access to your own online meeting room and virtual collaboration platform ($1,200).</li>
    <li class="service service--5">Repurposing for Online Audiences: Design and develop materials, agenda, event plans and activities to repurpose your face-to-face session for online sessions that market your expertise. Includes 2-hours of One-on-One online coaching to learn about web conferencing tools and how to use them for your business ($500).</li>
    <li class="service service--6">One-on-one coaching with resources: 2-hours of One-on-One online coaching to learn about web conferencing tools and how to use them for your business. Includes access to online resource library of our Online Facilitator Certification ($300).</li>
    <li class="service service--7">One-on-one coaching: 2-hours of One-on-One online coaching to learn about web conferencing tools and how to use them for your business. Includes three job aids for online facilitators ($200)</li>
  </ul>

  <div class="closing">
    <p>You'll participate via the LiveRoom Meeting platform. No special software is required. If you have a computer with Internet access and a direct telephone line you have all is needed to participate.</p>
    <p>As a professional communicators – whether you are a small business owner, an educator or a manager - you know that webinar technology is here to stay. Have you wondered how to use them to benefit your business or your organization? Leave the details to us. Well implemented online sessions can give your business unparalleled access to new markets and potential new clients at a minimum cost.</p>
  </div>

  <div class="contact-bar">Want to know more? <strong>Call us at</strong> <span class="contact-bar__phone">202-555-0148</span></div>
</section>

</body>
</html>
```